Venture Capital Firm Needs Website Redesign

We need a bold revamp of our website (https://halvenmoor.vc/)
which at the moment looks washed out. We want a crisp, fresh and unique look. Feel free to keep as much or as little content in the site. The only thing we need to keep is a team section. The site should convey a clear distinction between our 3 product lines: Venture Capital, Private Credit, and Crypto. Two versions of our logo are attached and they should not change. For design inspirations, we like http://www.plumridgecap.com/ for a more simple site and for a more built out site we like http://tallowgate.com/

Updates
Industry/Entity Type
Investment
Coding
Coded - Design and coding required
Number of Pages Required
1 page
Font styles to use
Colors
Designer to choose colors to be used in the design.
Requirements
Must have
- - Clear distinction between our 3 product lines: Venture Capital, Private Credit
- - Team section

Nice to have
- Some really creative aspect like http://www.plumridgecap.com/ has with the distinction between first, second, and third kind

```html
<!DOCTYPE html>
<html lang="en">
<head>
<meta charset="utf-8">
<title>Halvenmoor</title>
<link rel="stylesheet" href="https://fonts.googleapis.com/css2?family=Poppins:wght@400;500;600;700;800&display=swap">
<style>
:root{
  --green:#7a952e;
  --green-light:#a7bf5a;
  --ink:#222222;
  --muted:#555555;
  --hero-top:#ffffff;
  --hero-bottom:#eef3dc;
  --band:#f2f4f9;
  --footer:#f1f2f8;
  --rule:#8aa23a;
  --ring:#c9ccb2;
}
*{box-sizing:border-box;margin:0;padding:0}
html,body{width:1200px;height:2546px;overflow:hidden}
body{position:relative;font-family:'Poppins',sans-serif;color:var(--ink);background:#fff}
.abs{position:absolute}
.hero{left:0;top:0;width:1200px;height:642px;background:linear-gradient(180deg,var(--hero-top) 0%,var(--hero-bottom) 100%)}
.hero-edge{left:-30px;top:371px;width:54px;height:58px;border-radius:50%;background:#e6e6e6}
.brand{display:flex;align-items:center;gap:13px;font-weight:400;font-size:22px;letter-spacing:.5px;color:var(--ink)}
.brand-dot{width:52px;height:52px;border:2px solid var(--ink);border-radius:50%}
.site-brand{left:161px;top:48px}
.nav{left:506px;top:66px;width:533px;display:flex;justify-content:space-between;font-size:12.5px;font-weight:400;letter-spacing:.4px}
.hero-title{left:161px;top:178px;font-size:34px;line-height:46px;font-weight:800;text-transform:uppercase;color:var(--ink)}
.hero-title .accent{color:var(--green)}
.hero-art{left:594px;top:144px;width:540px;height:430px}
.slider{left:512px;top:571px;display:flex;gap:4px}
.slider span{width:42px;height:4px;background:#6d6d6d}
.slider span.on{background:#dfe8b8;border:1px solid #b9c97a}
.rule{width:114px;height:3px;background:var(--rule)}
.section-title{width:1200px;text-align:center;font-size:27px;font-weight:700;letter-spacing:.3px}
.tile{position:absolute}
.tile-green{background:var(--green);color:#fff;font-weight:700;font-size:28px;line-height:32px;padding:0 44px;display:flex;align-items:center}
.team-bg{left:0;top:1420px;width:1200px;height:800px;background:linear-gradient(180deg,#ffffff 0%,#f4f6ea 30%,#e9eed3 60%,#dfe7c0 100%)}
.member{width:240px;text-align:center}
.member-name{font-size:17px;font-weight:500;margin-top:4px}
.member-role{font-size:12px;color:var(--muted)}
.btn{display:flex;align-items:center;justify-content:center;font-size:12px;font-weight:600;letter-spacing:1px;text-transform:uppercase}
.btn-solid{background:var(--green);color:#fff}
.btn-line{border:2px solid var(--green);color:var(--green);background:#fff}
.cta-title{left:161px;top:2100px;font-size:24px;color:var(--green)}
.cta-sub{left:161px;top:2143px;font-size:15px}
.footer{left:0;top:2216px;width:1200px;height:330px;background:var(--footer);border-top:1px solid #dde0ea}
.footer-brand{left:161px;top:2262px}
.address{left:161px;top:2318px;font-size:12.5px;line-height:21px}
.socials{left:161px;top:2416px;display:flex;gap:11px}
.socials span{width:14px;height:14px;border-radius:50%;background:#a4a8b4}
.col{font-size:11.5px;line-height:21px;color:#4a4a4a}
.col h4{font-size:13px;font-weight:500;color:var(--ink);letter-spacing:.6px;margin-bottom:22px}
.copyright{left:0;top:2496px;width:1200px;text-align:center;font-size:10.5px;letter-spacing:.3px}
</style>
</head>
<body>

<div class="abs hero"></div>
<div class="abs hero-edge"></div>
<div class="abs brand site-brand"><span class="brand-dot"></span>HALVENMOOR</div>
<nav class="abs nav"><span>VENTURE</span><span>PRIVATE CREDIT</span><span>CRYPTO</span><span>ABOUT US</span><span>TEAM</span><span>BLOG</span></nav>
<h1 class="abs hero-title"><span class="accent">Halvenmoor</span><br>operates at the<br>intersection<br>of technology<br>and <span class="accent">novel<br>asset classes.</span></h1>
<div class="abs hero-art" role="img" aria-label="Isometric illustration of an office room with people working at desks and screens" style="background:radial-gradient(ellipse 40% 22% at 55% 58%,rgba(255,255,255,.55),rgba(255,255,255,0)),radial-gradient(ellipse 60% 30% at 50% 78%,#8fad3c,rgba(143,173,60,0)),linear-gradient(180deg,#f1f1f1 0%,#dcdcdc 35%,#c7d79a 52%,#9fbb4e 68%,#6f8a28 100%);clip-path:polygon(50% 0,100% 20%,100% 77%,50% 100%,0 77%,0 20%)"></div>
<div class="abs slider"><span></span><span></span><span class="on"></span><span></span></div>

<div class="abs rule" style="left:543px;top:686px"></div>
<h2 class="abs section-title" style="left:0;top:706px">OUR PRODUCTS</h2>

<div class="tile tile-green" style="left:161px;top:794px;width:285px;height:200px">VENTURE<br>CAPITAL</div>
<div class="tile" role="img" aria-label="Black and white photo of a hand holding a pen over a tablet" style="left:457px;top:794px;width:285px;height:387px;background:radial-gradient(ellipse 45% 40% at 62% 30%,#f4f4f4,rgba(244,244,244,0)),radial-gradient(ellipse 70% 35% at 40% 80%,#1e1e1e,rgba(30,30,30,0)),linear-gradient(160deg,#d8d8d8 0%,#bdbdbd 45%,#555 80%,#e6e6e6 100%)"></div>
<div class="tile tile-green" style="left:753px;top:794px;width:284px;height:200px">CRYPTO</div>
<div class="tile" role="img" aria-label="Black and white photo of a hand stacking coins" style="left:161px;top:1005px;width:285px;height:388px;background:radial-gradient(ellipse 45% 30% at 65% 15%,#cfcfcf,rgba(207,207,207,0)),radial-gradient(ellipse 35% 45% at 45% 70%,#6a6a6a,rgba(106,106,106,0)),linear-gradient(180deg,#f2f2f2 0%,#e0e0e0 40%,#9a9a9a 75%,#7c7c7c 100%)"></div>
<div class="tile tile-green" style="left:457px;top:1193px;width:285px;height:200px">PRIVATE<br>CREDIT</div>
<div class="tile" role="img" aria-label="Black and white photo of a coin in front of a market price board" style="left:753px;top:1005px;width:284px;height:388px;background:radial-gradient(circle 95px at 48% 62%,#bdbdbd,#8a8a8a 70%,rgba(60,60,60,0)),linear-gradient(180deg,#1c1c1c 0%,#2e2e2e 40%,#3a3a3a 75%,#555 100%)"></div>

<div class="abs team-bg"></div>
<div class="abs rule" style="left:543px;top:1482px"></div>
<h2 class="abs section-title" style="left:0;top:1502px">OUR TEAM</h2>

<svg class="abs" style="left:0;top:1590px" width="1200" height="180" viewBox="0 0 1200 180">
  <defs>
    <radialGradient id="portrait" cx="50%" cy="40%" r="60%">
      <stop offset="0%" stop-color="#d4d4d4"/>
      <stop offset="45%" stop-color="#a6a6a6"/>
      <stop offset="100%" stop-color="#3c3c3c"/>
    </radialGradient>
  </defs>
  <g fill="none" stroke="var(--ring)" stroke-width="3">
    <circle cx="258" cy="90" r="86"/><circle cx="485" cy="90" r="86"/><circle cx="713" cy="90" r="86"/><circle cx="940" cy="90" r="86"/>
  </g>
  <g fill="var(--ring)">
    <circle cx="172" cy="90" r="8"/><circle cx="344" cy="90" r="8"/>
    <circle cx="399" cy="90" r="8"/><circle cx="571" cy="90" r="8"/>
    <circle cx="627" cy="90" r="8"/><circle cx="799" cy="90" r="8"/>
    <circle cx="854" cy="90" r="8"/><circle cx="1026" cy="90" r="8"/>
  </g>
  <g fill="url(#portrait)">
    <circle cx="258" cy="90" r="79" role="img" aria-label="Portrait photo of Oren Castell"/>
    <circle cx="485" cy="90" r="79" role="img" aria-label="Portrait photo of Rohan Vedley"/>
    <circle cx="713" cy="90" r="79" role="img" aria-label="Portrait photo of Samir Dunthorpe"/>
    <circle cx="940" cy="90" r="79" role="img" aria-label="Portrait photo of Tessa Marwick"/>
  </g>
</svg>
<div class="abs member" style="left:138px;top:1778px"><div class="member-name">Oren Castell</div><div class="member-role">Partner</div></div>
<div class="abs member" style="left:365px;top:1778px"><div class="member-name">Rohan Vedley</div><div class="member-role">Partner</div></div>
<div class="abs member" style="left:593px;top:1778px"><div class="member-name">Samir Dunthorpe</div><div class="member-role">Partner</div></div>
<div class="abs member" style="left:820px;top:1778px"><div class="member-name">Tessa Marwick</div><div class="member-role">Community Manager</div></div>

<div class="abs btn btn-solid" style="left:524px;top:1867px;width:151px;height:42px">View all team ›</div>

<svg class="abs" style="left:0;top:1960px" width="1200" height="260" viewBox="0 0 1200 260">
  <polygon points="0,85 373,12 1200,158 1200,260 0,260" fill="var(--band)"/>
</svg>
<div class="abs cta-title">Ready to get started?</div>
<div class="abs cta-sub">Get in touch, or create an account.</div>
<div class="abs btn btn-line" style="left:750px;top:2142px;width:152px;height:36px">Create account</div>
<div class="abs btn btn-solid" style="left:908px;top:2142px;width:129px;height:36px">Contact us</div>

<div class="abs footer"></div>
<svg class="abs" style="left:0;top:2340px" width="1200" height="206" viewBox="0 0 1200 206">
  <path d="M0 70 C150 20 260 90 400 60 C560 25 700 100 860 55 C1000 20 1100 70 1200 45 L1200 206 L0 206 Z" fill="#e6e8f3"/>
  <path d="M0 120 C180 80 320 140 500 110 C680 80 820 140 1000 105 C1100 90 1160 110 1200 100 L1200 206 L0 206 Z" fill="#ecedf6"/>
</svg>
<div class="abs brand footer-brand" style="font-size:19px;gap:10px"><span class="brand-dot" style="width:42px;height:42px"></span>HALVENMOOR</div>
<div class="abs address">info@halvenmoor.vc<br>418 Harlow Street, Suite 600<br>New York, NY 10003</div>
<div class="abs socials"><span></span><span></span><span></span><span></span><span></span></div>

<div class="abs col" style="left:434px;top:2256px"><h4>LINKS</h4>Payments<br>Subscriptions<br>Connect<br>Pricing<br>Works with Us<br>Global</div>
<div class="abs col" style="left:592px;top:2256px"><h4>DEVELOPERS</h4>Documentation<br>API reference<br>API status<br>Open source</div>
<div class="abs col" style="left:787px;top:2256px"><h4>COMPANY</h4>About<br>Customers<br>Jobs<br>Blog<br>Press</div>
<div class="abs col" style="left:945px;top:2256px"><h4>RESOURCES</h4>Support<br>Contact<br>Privacy &amp; terms</div>

<div class="abs copyright">© 2018 HALVENMOOR. ALL RIGHTS RESERVED. PRIVACY POLICY, TERMS AND CONDITIONS</div>

</body>
</html>
```